Business Card

We would like a very clean corporate, two sided business card that conveys that we are a quality focused, reliable organisation that can make a business better. We focus on a cycle of continuous improvement for IT systems.

The brief is primarily clean and corporate, nothing overly complicated.

We sell IT services, IT support, server implementation, problem solving services to businesses in Australia.

Business

```html
<!DOCTYPE html>
<html lang="en">
<head>
<meta charset="utf-8">
<title>Keystone Loop – Business Card</title>
<link rel="stylesheet" href="https://fonts.googleapis.com/css2?family=Exo+2:wght@400;500;600&display=swap">
<style>
  :root {
    --backdrop-light: #f4f4f4;
    --backdrop-dark: #b9b9b9;
    --paper: #e8e8e6;
    --paper-edge: #d9d9d6;
    --ink: #3a3a3a;
    --ink-dark: #1d1d28;
    --accent: #b0121b;
  }
  * { box-sizing: border-box; margin: 0; padding: 0; }
  html, body { width: 1200px; height: 900px; overflow: hidden; }
  body {
    position: relative;
    font-family: "Exo 2", sans-serif;
    color: var(--ink);
    background: radial-gradient(ellipse at 50% 45%, var(--backdrop-light) 0%, #dcdcdc 60%, var(--backdrop-dark) 100%);
  }
  .card {
    position: absolute;
    top: 290px;
    width: 520px;
    height: 290px;
    background: radial-gradient(circle at 40% 40%, var(--paper) 0%, var(--paper-edge) 100%);
    box-shadow: 3px 5px 8px rgba(0, 0, 0, 0.45);
  }
  .card--front { left: 60px; }
  .card--back { left: 620px; }

  .address {
    position: absolute;
    left: 58px;
    top: 62px;
    padding-left: 9px;
    border-left: 3px solid var(--accent);
    font-size: 16px;
    line-height: 20px;
  }
  .address .company { font-size: 18px; font-weight: 500; line-height: 22px; }
  .address .company em { font-style: normal; color: var(--accent); }

  .contact {
    position: absolute;
    right: 88px;
    top: 180px;
    font-size: 15px;
    line-height: 18px;
    font-weight: 500;
  }
  .contact .plus { color: var(--accent); }
  .abn {
    position: absolute;
    left: 262px;
    top: 232px;
    font-size: 11px;
    font-weight: 600;
  }
  .mark-square {
    display: inline-block;
    background: var(--accent);
  }
  .card--front .mark-square {
    position: absolute;
    right: 28px;
    top: 226px;
    width: 22px;
    height: 22px;
  }

  .wordmark {
    position: absolute;
    display: flex;
    align-items: center;
    gap: 14px;
  }
  .wordmark .name {
    font-weight: 500;
    color: var(--ink-dark);
    line-height: 0.9;
    text-align: right;
  }
  .card--back .wordmark { left: 176px; top: 98px; }
  .card--back .wordmark .name { font-size: 30px; }
  .card--back .wordmark .mark-square { width: 30px; height: 30px; }

  .wordmark--corner { right: 40px; bottom: 22px; }
  .wordmark--corner .name { font-size: 36px; }
  .wordmark--corner .mark-square { width: 34px; height: 34px; }
</style>
</head>
<body>
  <section class="card card--front" aria-label="Card front">
    <div class="address">
      <p class="company">Keystone <em>Loop</em> Pty Ltd</p>
      <p>Suite 210, 14-18 Harbour Lane</p>
      <p>North Sydney, NSW, 2061</p>
      <p>Australia</p>
    </div>
    <div class="contact">
      <p>PH: <span class="plus">+</span>61 2 9000 1234</p>
      <p>FAX: <span class="plus">+</span>61 2 9000 1289</p>
    </div>
    <p class="abn">ABN: 12 345 678 901</p>
    <span class="mark-square" aria-hidden="true"></span>
  </section>

  <section class="card card--back" aria-label="Card back">
    <div class="wordmark">
      <p class="name">keystone<br>loop</p>
      <span class="mark-square" aria-hidden="true"></span>
    </div>
  </section>

  <div class="wordmark wordmark--corner">
    <p class="name">keystone<br>loop</p>
    <span class="mark-square" aria-hidden="true"></span>
  </div>
</body>
</html>
```